Brochure Design Project

We need a brochure designed for our company, specifically targeted at our corporate business customers ... Banks, Financial Services, Government. The brochure needs to detail our services and what we have to offer.

It may be a brochure/booklet that we can give to clients when we meet them. It needs to have a very corporate look and feel and needs to align with our colour palette and logo.

Information is held on our website www.tessaroworldservices.com
Updates

Thank you everyone for being part of this project.  It was a very hard decision.

Target Market(s)

Corporate business and clients including banks, financial services, insurance and government.

Industry/Entity Type

Business

Requirements
Must have
• Must have a corporate and global feel to it.
Must have our logo and same or similar colour palette.

```html
<!DOCTYPE html>
<html lang="en">
<head>
<meta charset="utf-8">
<title>Tessaro World Services – Solutions Brochure</title>
<link rel="stylesheet" href="https://fonts.googleapis.com/css2?family=Bebas+Neue&family=Open+Sans:ital,wght@0,400;0,700;1,700&display=swap">
<style>
  :root {
    --stage: #cfcfcf;
    --blue: #2f95d8;
    --blue-light: #47a9e6;
    --blue-deep: #1a6db6;
    --ink-white: #ffffff;
    --silver-top: #f4f4f4;
    --silver-bottom: #9a9ea3;
    --photo-office-a: #cfd6dc;
    --photo-office-b: #7d8893;
    --photo-suit-a: #e9ecef;
    --photo-suit-b: #2c3440;
    --pie-red: #d8321f;
    --pie-green: #7cc63a;
    --pie-orange: #f49a12;
    --pie-blue: #3aa6e8;
  }
  * { box-sizing: border-box; margin: 0; padding: 0; }
  html, body { width: 1200px; height: 1000px; overflow: hidden; }
  body { background: var(--stage); font-family: "Open Sans", Arial, sans-serif; position: relative; }

  .spread { position: absolute; left: 60px; width: 1080px; height: 440px; display: flex; box-shadow: 0 6px 18px rgba(0,0,0,.25); }
  .spread--solutions { top: 40px; }
  .spread--sectors { top: 520px; }
  .page { position: relative; width: 540px; height: 100%; overflow: hidden; }

  .photo { position: absolute; }
  .photo--handshake { left: 0; top: 0; width: 370px; height: 440px; background: linear-gradient(135deg, var(--photo-suit-a) 0%, #c3c9cf 45%, var(--photo-suit-b) 100%); }
  .photo--signing { left: 0; top: 0; width: 300px; height: 440px; background: linear-gradient(160deg, #b9c2ca 0%, var(--photo-suit-b) 55%, #e8ebee 100%); }
  .photo--office { left: 0; top: 0; width: 250px; height: 440px; background: linear-gradient(150deg, var(--photo-office-a) 0%, #a8a49a 50%, var(--photo-office-b) 100%); }

  .contents-band { position: absolute; left: 370px; top: 0; width: 170px; height: 440px; background: var(--blue); }
  .contents-list { position: absolute; left: 348px; top: 70px; list-style: none; }
  .contents-item { display: flex; align-items: center; height: 60px; }
  .contents-item__num { width: 44px; height: 44px; border-radius: 50%; background: var(--blue); color: var(--ink-white); font-family: "Bebas Neue", Impact, sans-serif; font-size: 38px; line-height: 48px; text-align: center; }
  .contents-item__label { color: var(--ink-white); font-family: "Bebas Neue", Impact, sans-serif; font-size: 19px; margin-left: 2px; letter-spacing: .5px; }

  .section-title { position: absolute; font-family: "Bebas Neue", Impact, sans-serif; line-height: 1; letter-spacing: 1px; }
  .section-title--blue { color: var(--blue); text-shadow: 2px 2px 0 #fff, 3px 4px 6px rgba(0,0,0,.35); }
  .section-title--silver { background: linear-gradient(var(--silver-top), var(--silver-bottom)); -webkit-background-clip: text; background-clip: text; color: transparent; filter: drop-shadow(2px 3px 3px rgba(0,0,0,.45)); }
  .title-solutions { left: 34px; top: 300px; font-size: 64px; }
  .title-banking { left: 16px; top: 38px; font-size: 44px; }
  .title-business { left: 36px; top: 344px; font-size: 84px; }
  .title-community { left: 16px; top: 34px; font-size: 52px; }

  .quote { position: absolute; color: var(--ink-white); font-weight: 700; font-style: italic; font-size: 9.5px; line-height: 1.2; text-shadow: 1px 1px 2px rgba(0,0,0,.4); }
  .quote--solutions { left: 34px; top: 364px; width: 300px; }
  .quote--banking { left: 16px; top: 86px; width: 270px; }
  .quote--business { left: 38px; top: 326px; width: 250px; }
  .quote--community { left: 16px; top: 86px; width: 230px; }

  .text-column { position: absolute; top: 0; height: 440px; background: var(--blue); color: var(--ink-white); padding: 34px 16px 0; font-size: 6.6px; line-height: 1.3; }
  .text-column--banking { left: 300px; width: 240px; }
  .text-column--community { left: 250px; width: 290px; padding-top: 30px; }
  .text-column h2, .business-copy h2 { font-size: 8.5px; font-weight: 700; margin-bottom: 8px; }
  .text-column p, .business-copy p { margin-bottom: 8px; }

  .page--business { background: linear-gradient(180deg, var(--blue-light) 0%, var(--blue) 50%, var(--blue-deep) 100%); }
  .pie-chart { position: absolute; left: 26px; top: 34px; }
  .business-copy { position: absolute; left: 290px; top: 34px; width: 230px; color: var(--ink-white); font-size: 6.6px; line-height: 1.3; }

  .page-number { position: absolute; bottom: 10px; color: var(--ink-white); font-size: 8px; }
  .page-number--left { left: 14px; }
  .page-number--right { left: 14px; color: #333; }
</style>
</head>
<body>

<section class="spread spread--solutions">
  <article class="page page--solutions">
    <div class="photo photo--handshake" role="img" aria-label="Photo of business people stacking hands together in agreement"></div>
    <div class="contents-band"></div>
    <ol class="contents-list">
      <li class="contents-item"><span class="contents-item__num">1</span><span class="contents-item__label">Banking &amp; Finance</span></li>
      <li class="contents-item"><span class="contents-item__num">2</span><span class="contents-item__label">Business</span></li>
      <li class="contents-item"><span class="contents-item__num">3</span><span class="contents-item__label">Community</span></li>
      <li class="contents-item"><span class="contents-item__num">4</span><span class="contents-item__label">Environment</span></li>
      <li class="contents-item"><span class="contents-item__num">5</span><span class="contents-item__label">Global</span></li>
    </ol>
    <h1 class="section-title section-title--blue title-solutions">Solutions</h1>
    <p class="quote quote--solutions">“Everything should be made as simple as possible, but not one bit simpler.” - Alden Everhart</p>
  </article>

  <article class="page page--banking">
    <div class="photo photo--signing" role="img" aria-label="Photo of a hand stamping a signed contract on a desk"></div>
    <h1 class="section-title section-title--silver title-banking">Banking &amp; Finance</h1>
    <p class="quote quote--banking">“Everything that can be counted does not necessarily count; everything that counts cannot necessarily be counted.” - Alden Everhart</p>
    <div class="text-column text-column--banking">
      <h2>Banking &amp; Finance</h2>
      <p>Our specialist team has extensive experience across all areas within Banking &amp; Financial Services.</p>
      <p>Whether you are optimising or transforming an existing business or creating something totally new we can assist. Many of our models and systems have been designed specifically for this industry. They support all elements of business including</p>
      <p>Increasing customer satisfaction<br>Enhancing employee satisfaction<br>Improving revenue<br>Reducing cost<br>Our approach to solutions is based on</p>
      <p>A multi-dimensional view of the business<br>Understanding the “whole” system to ensure all impacts are managed<br>The belief that everything is connected and therefore ALL need to be accounted for within the change<br>Ensuring the People and Customer element is understood and supported throughout the transition.<br>We are different because</p>
      <p>We specialise in working with ambiguity and complexity<br>We challenge current thinking and paradigms<br>We remove complexity, we don't add to it<br>We understand how it works today to create how it works tomorrow<br>We monitor and measure the sustainability of the solution</p>
    </div>
  </article>
</section>

<section class="spread spread--sectors">
  <article class="page page--business">
    <svg class="pie-chart" width="260" height="260" viewBox="0 0 260 260" role="img" aria-label="Pie chart in four segments">
      <path d="M130 130 L20 130 A110 110 0 0 1 167.6 26.6 Z" fill="var(--pie-red)"/>
      <path d="M134 126 L171.6 22.6 A110 110 0 0 1 242.3 106.9 Z" fill="var(--pie-green)"/>
      <path d="M138 134 L246.3 114.9 A110 110 0 0 1 193 229.3 Z" fill="var(--pie-orange)"/>
      <path d="M130 130 L185 225.3 A110 110 0 0 1 20 130 Z" fill="var(--pie-blue)"/>
    </svg>
    <div class="business-copy">
      <h2>Business</h2>
      <p>Our specialist team has extensive experience across all areas of Business.</p>
      <p>Whether you are optimising or transforming an existing business or creating something totally new we can assist.</p>
      <p>Many of our models and systems have been designed specifically for this industry. They support all elements of business including</p>
      <p>Increasing customer satisfaction<br>Enhancing employee satisfaction<br>Improving revenue<br>Reducing cost<br>Our approach to solutions is based on</p>
      <p>A multi-dimensional view of the business<br>Understanding the “whole” system to ensure all impacts are managed<br>The belief that everything is connected and therefore ALL need to be accounted for within the change<br>- Ensuring the People and Customer element is understood and supported throughout the transition.<br>We are different because</p>
      <p>We specialise in working with ambiguity and complexity<br>We challenge current thinking and paradigms<br>We remove complexity, we don't add to it<br>We understand how it works today to create how it works tomorrow<br>We monitor and measure the sustainability of the solution</p>
    </div>
    <p class="quote quote--business">“Health not wealth is the determinant of true sustainability.”</p>
    <h1 class="section-title section-title--silver title-business">Business</h1>
    <span class="page-number page-number--left">9</span>
  </article>

  <article class="page page--community">
    <div class="photo photo--office" role="img" aria-label="Photo of a woman working at a desk in a bright office"></div>
    <h1 class="section-title section-title--blue title-community">Community</h1>
    <p class="quote quote--community">“A nations culture resides in the heart and in the soul of its people.” - Mohan Varela</p>
    <span class="page-number page-number--right">10</span>
    <div class="text-column text-column--community">
      <h2>Community</h2>
      <p>There are many issues that impact all areas of our community. These issues have many causes which in turn can impact many other areas of the community such as:-</p>
      <p>Homelessness<br>Mental Health<br>Judicial System<br>Welfare System<br>Elderly Community<br>Indigenous Community<br>Juveniles and many others<br>To create a sustainable solution all aspects of the community system need to be understood and managed as a ‘whole’ system.</p>
      <p>Tessaro World Services specialise in working with complex problems that are multi-layered and have numerous interdependencies.</p>
      <p>Our approach to problem solving is holistic ensuring that the ‘whole’ system is understood and managed. We have found that if you impact one thing, you impact everything; therefore sustainable solutions for the Community must encompass all aspects of the community.</p>
    </div>
  </article>
</section>

</body>
</html>
```